Company Stationary, Business Card, Enevelopes, Letterhead
Would also like note stationary, and enevelope to fit
Company Stationary, Business Card, Enevelopes, Letterhead - Real Estate
Creative Brief
Professional
Dale Harwick
Designated Broker/Owner
2716 Juniper Loop Ste 214 West Richland, WA. 99417
dale@brightfieldhomepartners.net
www.brightfieldhomepartners.net

```html
<!DOCTYPE html>
<html lang="en">
<head>
<meta charset="utf-8">
<title>Brightfield Home Partners – Stationery Set</title>
<link href="https://fonts.googleapis.com/css2?family=Montserrat:wght@400;700&display=swap" rel="stylesheet">
<style>
:root{
  --board:#4a4b4d;
  --board-dark:#2e2f31;
  --red:#c3141c;
  --red-dark:#7d0b10;
  --paper:#ffffff;
  --ink:#3a3a3a;
  --grey:#8a8b8d;
  --charcoal:#2a2a2c;
}
*{margin:0;padding:0;box-sizing:border-box}
html,body{width:1200px;height:233px;overflow:hidden}
body{background:radial-gradient(ellipse at 50% 45%,var(--board) 0%,var(--board-dark) 100%);font-family:'Montserrat',sans-serif;position:relative}
.item{position:absolute;background:var(--paper);box-shadow:0 2px 5px rgba(0,0,0,.45);overflow:hidden}
.item.dark{background:linear-gradient(160deg,#4a4a4c,var(--charcoal))}
.item.red{background:linear-gradient(150deg,var(--red),var(--red-dark))}
.swoosh{position:absolute;left:0;width:100%}
.brand{display:flex;align-items:center;gap:3px;position:absolute;color:var(--red);font-weight:700;letter-spacing:.3px;white-space:nowrap}
.brand .dot{border-radius:50%;background:currentColor;flex:none}
.brand.light{color:#fff}
.brand.s{font-size:5px}.brand.s .dot{width:5px;height:5px}
.brand.m{font-size:7px}.brand.m .dot{width:7px;height:7px}
.brand.l{font-size:10px}.brand.l .dot{width:10px;height:10px}
.contact{position:absolute;font-size:3.2px;line-height:4.3px;color:var(--ink)}
.contact.light{color:#eee}
.contact b{font-size:4.2px;color:var(--red)}
.contact.light b{color:#fff}
.photo{position:absolute;background:linear-gradient(180deg,#9a9ca0,#5d5f63)}
.flap{position:absolute;top:0;left:0;width:100%}
</style>
</head>
<body>

<!-- business cards: dark column -->
<div class="item dark" style="left:7px;top:30px;width:101px;height:58px">
  <div class="brand light m" style="left:14px;top:24px"><span class="dot"></span>BRIGHTFIELD</div>
</div>
<div class="item dark" style="left:7px;top:98px;width:101px;height:58px">
  <svg class="swoosh" style="bottom:0;height:18px" viewBox="0 0 100 18" preserveAspectRatio="none"><path d="M0 8 Q50 -2 100 10 L100 18 L0 18Z" fill="var(--red)"/></svg>
  <div class="photo" role="img" aria-label="Portrait of the broker" style="left:6px;top:8px;width:20px;height:26px"></div>
  <div class="contact light" style="left:31px;top:10px"><b>Dale Harwick</b><br>Designated Broker/Owner<br>Office 509.555.0142<br>dale@brightfieldhomepartners.net</div>
</div>
<div class="item dark" style="left:7px;top:166px;width:101px;height:58px">
  <svg class="swoosh" style="top:0;height:16px" viewBox="0 0 100 16" preserveAspectRatio="none"><path d="M0 0 L100 0 L100 6 Q50 18 0 8Z" fill="var(--red)"/></svg>
  <div class="brand light s" style="left:28px;top:30px"><span class="dot"></span>BRIGHTFIELD</div>
</div>

<!-- business cards: white column -->
<div class="item" style="left:115px;top:30px;width:108px;height:58px">
  <svg class="swoosh" style="top:0;height:20px" viewBox="0 0 100 20" preserveAspectRatio="none"><path d="M0 0 L100 0 L100 8 Q50 22 0 10Z" fill="var(--red)"/></svg>
  <div class="brand m" style="left:22px;top:30px"><span class="dot"></span>BRIGHTFIELD</div>
</div>
<div class="item" style="left:115px;top:98px;width:108px;height:58px">
  <svg class="swoosh" style="bottom:0;height:14px" viewBox="0 0 100 14" preserveAspectRatio="none"><path d="M0 6 Q50 -2 100 8 L100 14 L0 14Z" fill="var(--red)"/></svg>
  <div class="photo" role="img" aria-label="Portrait of the broker" style="left:6px;top:7px;width:20px;height:27px"></div>
  <div class="contact" style="left:31px;top:8px"><b>Dale Harwick</b><br>Designated Broker/Owner<br>2716 Juniper Loop Ste 214<br>West Richland, WA. 99417<br>Mobile 509.555.0187</div>
</div>
<div class="item" style="left:115px;top:166px;width:108px;height:58px">
  <svg class="swoosh" style="top:0;height:12px" viewBox="0 0 100 12" preserveAspectRatio="none"><path d="M0 0 L100 0 L100 4 Q50 14 0 6Z" fill="var(--red)"/></svg>
  <div class="contact" style="left:10px;top:22px">www.brightfieldhomepartners.net<br>dale@brightfieldhomepartners.net</div>
</div>

<!-- letterheads -->
<div class="item" style="left:240px;top:10px;width:110px;height:212px">
  <svg class="swoosh" style="top:0;height:42px" viewBox="0 0 100 42" preserveAspectRatio="none"><path d="M0 0 L100 0 L100 14 Q55 46 0 24Z" fill="var(--red)"/><path d="M0 24 Q55 46 100 14 L100 18 Q55 50 0 28Z" fill="var(--grey)"/></svg>
  <div class="brand s" style="left:34px;top:44px"><span class="dot"></span>BRIGHTFIELD</div>
  <svg class="swoosh" style="bottom:0;height:14px" viewBox="0 0 100 14" preserveAspectRatio="none"><path d="M0 8 Q50 0 100 6 L100 14 L0 14Z" fill="var(--red)"/></svg>
</div>
<div class="item" style="left:365px;top:10px;width:110px;height:212px">
  <svg class="swoosh" style="top:0;height:26px" viewBox="0 0 100 26" preserveAspectRatio="none"><path d="M0 0 L100 0 L100 10 Q50 28 0 14Z" fill="var(--red)"/></svg>
  <div class="brand s" style="left:34px;top:30px"><span class="dot"></span>BRIGHTFIELD</div>
  <svg class="swoosh" style="bottom:0;height:24px" viewBox="0 0 100 24" preserveAspectRatio="none"><path d="M0 14 Q50 0 100 12 L100 24 L0 24Z" fill="var(--red)"/></svg>
</div>

<!-- note cards -->
<div class="item" style="left:492px;top:40px;width:110px;height:42px">
  <svg class="swoosh" style="top:0;height:12px" viewBox="0 0 100 12" preserveAspectRatio="none"><path d="M0 0 L100 0 L100 4 Q50 14 0 6Z" fill="var(--red)"/></svg>
  <div class="brand s" style="left:8px;top:16px"><span class="dot"></span>BRIGHTFIELD</div>
</div>
<div class="item" style="left:618px;top:40px;width:102px;height:42px">
  <svg class="swoosh" style="bottom:0;height:12px" viewBox="0 0 100 12" preserveAspectRatio="none"><path d="M0 6 Q50 -2 100 6 L100 12 L0 12Z" fill="var(--red)"/></svg>
  <div class="brand s" style="left:30px;top:14px"><span class="dot"></span>BRIGHTFIELD</div>
</div>

<!-- small envelopes -->
<div class="item" style="left:492px;top:96px;width:110px;height:48px">
  <svg class="flap" style="height:30px" viewBox="0 0 100 30" preserveAspectRatio="none"><path d="M0 0 L100 0 L100 8 Q50 34 0 8Z" fill="var(--red)"/></svg>
  <div class="brand s" style="left:6px;top:34px"><span class="dot"></span>BRIGHTFIELD</div>
</div>
<div class="item dark" style="left:618px;top:96px;width:102px;height:48px">
  <svg class="flap" style="height:28px" viewBox="0 0 100 28" preserveAspectRatio="none"><path d="M0 0 L50 26 L100 0Z" fill="var(--red)"/></svg>
</div>

<!-- large envelopes -->
<div class="item" style="left:735px;top:34px;width:148px;height:80px">
  <svg class="flap" style="height:30px" viewBox="0 0 100 30" preserveAspectRatio="none"><path d="M0 0 L100 0 L100 6 Q50 34 0 6Z" fill="var(--red)"/></svg>
  <div class="brand s" style="left:8px;top:40px"><span class="dot"></span>BRIGHTFIELD</div>
  <div class="contact" style="left:8px;top:50px">2716 Juniper Loop Ste 214<br>West Richland, WA. 99417</div>
</div>
<div class="item" style="left:735px;top:128px;width:148px;height:82px">
  <svg class="flap" style="height:46px" viewBox="0 0 100 46" preserveAspectRatio="none"><path d="M0 0 L50 44 L100 0Z" fill="#f2f2f2" stroke="#d5d5d5" stroke-width=".6"/></svg>
  <svg class="swoosh" style="bottom:0;height:14px" viewBox="0 0 100 14" preserveAspectRatio="none"><path d="M0 8 Q50 0 100 6 L100 14 L0 14Z" fill="var(--red)"/></svg>
</div>

<!-- presentation folder -->
<div class="item red" style="left:900px;top:10px;width:145px;height:212px">
  <svg class="swoosh" style="bottom:40px;height:40px" viewBox="0 0 100 40" preserveAspectRatio="none"><path d="M0 30 Q50 0 100 20 L100 26 Q50 6 0 36Z" fill="rgba(255,255,255,.15)"/></svg>
</div>
<div class="item" style="left:1045px;top:10px;width:148px;height:212px;background:linear-gradient(180deg,#fff 60%,#eee)">
  <svg class="swoosh" style="top:0;height:70px" viewBox="0 0 100 70" preserveAspectRatio="none"><path d="M0 0 L100 0 L100 30 Q50 80 0 40Z" fill="var(--red)"/></svg>
  <div class="brand m" style="left:24px;top:96px"><span class="dot"></span>BRIGHTFIELD</div>
  <svg class="swoosh" style="bottom:0;height:50px" viewBox="0 0 100 50" preserveAspectRatio="none"><path d="M0 20 Q50 0 100 14 L100 50 L0 50Z" fill="var(--red)"/></svg>
  <div class="item" style="left:86px;top:176px;width:50px;height:26px">
    <div class="contact" style="left:3px;top:4px"><b>Dale Harwick</b><br>Broker/Owner</div>
  </div>
</div>

</body>
</html>
```